Occupational Therapist does home accessibility for disabled folks; needs business card design

We need a business card for a company in Portland, Oregon that specializes in making homes accessible, comfortable, and functional for people who are disabled or aging who would like to stay in THEIR home. Our medical background as Occupational Therapists allows us to translate the functional needs of the person into the recommendations for the design of the home remodel.

Target Market(s)

Elderly, children of elderly
People with disabilities, families of people with disabilities

Industry/Entity Type

Business

Contact Information for Business Card

Company name: HomeWise
Name: Danielle Reyes Crawford, OTR/L, CAPS, ECHM
Occupational Therapist, Home Modification & Accessibility Specialist
website: www.homewiseforyears.com
email: homewiseforyears@nestmail.example
phone: (503)218-4057
CCB #: 487315

Font styles to use
Sans Serif

Requirements
Must have
• My logo
• Easy to read font with contrasting background
• Please list the Services offered: Occupational Therapy, Home safety & accessibility assessments, Home modification consulting, project management
Nice to have
• Friendly, welcoming feel
Should not have
• Dark colored background

```html
<!DOCTYPE html>
<html lang="en">
<head>
<meta charset="utf-8">
<title>HomeWise Business Card</title>
<link href="https://fonts.googleapis.com/css2?family=Lato:wght@300;400;700&display=swap" rel="stylesheet">
<style>
  :root {
    --orange: #d06f05;
    --slate: #566262;
    --stage: #f2f4f3;
    --frame: #ffffff;
    --offset: #e6ecec;
    --paper: #ffffff;
  }
  html, body { margin: 0; padding: 0; overflow: hidden; }
  body { width: 1200px; height: 1200px; background: var(--frame); font-family: "Lato", sans-serif; }
  .canvas { position: relative; width: 1200px; height: 1200px; overflow: hidden; }
  .artwork { position: absolute; left: 0; top: 0; width: 1200px; height: 1200px; }
  .txt { position: absolute; margin: 0; white-space: nowrap; line-height: 1; }
  .brand { color: var(--slate); font-weight: 700; letter-spacing: -0.5px; display: flex; align-items: center; gap: 9px; }
  .brand .mark { display: inline-block; background: var(--orange); }
  .brand--front { left: 356px; top: 292px; font-size: 31px; }
  .brand--front .mark { width: 15px; height: 15px; }
  .brand--back { left: 468px; top: 798px; font-size: 56px; }
  .brand--back .mark { width: 26px; height: 26px; }
  .service { left: 351px; font-size: 16px; font-weight: 300; color: var(--slate); letter-spacing: 0.2px; }
  .info-panel { position: absolute; left: 647px; top: 218px; width: 252px; height: 312px; overflow: hidden; }
  .holder-name { left: 22px; top: 46px; font-size: 14px; font-weight: 400; color: #fff; letter-spacing: 0.1px; }
  .holder-creds { left: 24px; top: 66px; font-size: 12.5px; font-weight: 300; color: #fff; }
  .contact { left: 33px; font-size: 11.5px; font-weight: 300; color: #fff; letter-spacing: 0.3px; }
</style>
</head>
<body>
<div class="canvas">
  <svg class="artwork" viewBox="0 0 1500 1500" aria-hidden="true">
    <rect x="35" y="35" width="1430" height="1430" fill="var(--stage)"/>

    <g class="card-front">
      <rect x="393" y="255" width="745" height="425" fill="var(--paper)"/>
      <polygon points="790,258 768,333 690,333 690,392 735,392 708,468 790,670" fill="var(--offset)"/>
      <polygon points="795,283 770,345 707,345 707,400 748,400 722,468 795,655" fill="var(--orange)"/>
      <rect x="809" y="272" width="315" height="390" fill="var(--orange)"/>
      <rect x="393" y="472" width="37" height="13" fill="var(--slate)"/>
      <rect x="393" y="499" width="37" height="13" fill="var(--slate)"/>
      <rect x="393" y="526" width="37" height="13" fill="var(--slate)"/>
      <path d="M829,524 l3,-1 l2,4 l-2,2 q1,3 4,5 l2,-2 l4,2 l-1,3 q-8,1 -12,-13 z" fill="#fff"/>
      <rect x="826" y="560" width="11" height="8" fill="#fff"/>
      <polyline points="826,560 831.5,565 837,560" fill="none" stroke="var(--orange)" stroke-width="1"/>
      <circle cx="831.5" cy="597" r="5.5" fill="none" stroke="#fff" stroke-width="1.3"/>
      <ellipse cx="831.5" cy="597" rx="2.3" ry="5.5" fill="none" stroke="#fff" stroke-width="1"/>
      <line x1="826" y1="597" x2="837" y2="597" stroke="#fff" stroke-width="1"/>
    </g>

    <g class="card-back">
      <rect x="397" y="823" width="745" height="425" fill="var(--paper)"/>
      <polygon points="397,823 1125,823 1119,838 397,838" fill="var(--slate)"/>
      <polygon points="397,1233 1116,1233 1122,1248 397,1248" fill="var(--orange)"/>
      <polygon points="1142,823 1142,1248 1135,1248 1057,1037 1085,962 1040,962 1040,900 1110,900" fill="var(--orange)"/>
    </g>
  </svg>

  <p class="txt brand brand--front"><span>HomeWise</span><span class="mark"></span></p>
  <p class="txt service" style="top:375px">HOME MODIFICATION</p>
  <p class="txt service" style="top:397px">OCCUPATIONAL THERAPIST</p>
  <p class="txt service" style="top:419px">ACCESSIBILITY SPECIALIST</p>

  <div class="info-panel">
    <p class="txt holder-name">DANIELLE REYES CRAWFORD</p>
    <p class="txt holder-creds">OTR/L, CAPS, ECHM</p>
    <p class="txt contact" style="top:201px">(503)218-4057</p>
    <p class="txt contact" style="top:228px">homewiseforyears@nestmail.example</p>
    <p class="txt contact" style="top:252px">www.homewiseforyears.com</p>
  </div>

  <p class="txt brand brand--back"><span>HomeWise</span><span class="mark"></span></p>
</div>
</body>
</html>
```